Business cards design on a high standard

We advise clients on insurance and financial matters, since these clients pay for our advice, the design should have a high standard. Our logo should be included. From the colors we are open for everything.

Colors

Designer to choose colors to be used in the design.

```html
<!DOCTYPE html>
<html lang="en">
<head>
<meta charset="utf-8">
<title>Alpine Counsel – Business Cards</title>
<link rel="stylesheet" href="https://fonts.googleapis.com/css2?family=Saira:wght@500;600&family=Nunito:wght@400;700&display=swap">
<style>
  :root {
    --stage: #1c1c1e;
    --card-dark: #151517;
    --card-light: #ffffff;
    --brand-red: #e0232b;
    --text-grey: #7d7d80;
    --rule-grey: #9a9a9d;
  }
  * { box-sizing: border-box; margin: 0; padding: 0; }
  html, body { width: 1200px; height: 900px; overflow: hidden; }
  body {
    background: var(--stage);
    position: relative;
    font-family: "Nunito", sans-serif;
  }
  .card {
    position: absolute;
    left: 250px;
    width: 700px;
    height: 400px;
    overflow: hidden;
    box-shadow: 0 10px 30px rgba(0,0,0,.45);
  }
  .card--front { top: 35px; background: var(--card-dark); }
  .card--back { top: 465px; background: var(--card-light); }

  .brand-name {
    font-family: "Saira", sans-serif;
    font-weight: 600;
    color: var(--brand-red);
    letter-spacing: 3px;
    text-transform: uppercase;
    white-space: nowrap;
  }
  .card--front .brand-name {
    position: absolute;
    left: 0; right: 0; top: 172px;
    text-align: center;
    font-size: 44px;
  }

  .back-band { position: absolute; left: 0; top: 0; width: 700px; height: 210px; }
  .card--back .brand-name {
    position: absolute;
    right: 40px; top: 78px;
    font-size: 34px;
  }

  .holder {
    position: absolute;
    left: 370px; top: 228px;
  }
  .holder-name {
    font-family: "Saira", sans-serif;
    font-weight: 500;
    color: var(--brand-red);
    font-size: 22px;
    letter-spacing: 4px;
    text-transform: uppercase;
  }
  .holder-title {
    color: var(--text-grey);
    font-size: 17px;
    margin-top: -2px;
  }
  .holder-rule {
    position: absolute;
    left: 370px; top: 298px;
    width: 280px; height: 2px;
    background: var(--brand-red);
  }
  .contact-list {
    position: absolute;
    left: 370px; top: 318px;
    list-style: none;
  }
  .contact-item {
    display: flex;
    align-items: center;
    gap: 10px;
    color: var(--text-grey);
    font-size: 17px;
    line-height: 24px;
  }
  .contact-item svg { width: 16px; height: 16px; flex: none; }
  .web-domain { color: var(--brand-red); font-weight: 700; }
</style>
</head>
<body>

<section class="card card--front" aria-label="Card front">
  <div class="brand-name">Alpine Counsel</div>
</section>

<section class="card card--back" aria-label="Card back">
  <svg class="back-band" viewBox="0 0 700 210" aria-hidden="true">
    <path d="M0 0 H700 V205 H365 V125 H0 Z" fill="var(--card-dark)"/>
    <line x1="0" y1="122" x2="365" y2="122" stroke="#ffffff" stroke-width="1.5"/>
    <line x1="365" y1="208" x2="700" y2="208" stroke="var(--rule-grey)" stroke-width="2"/>
  </svg>
  <div class="brand-name">Alpine Counsel</div>

  <div class="holder">
    <div class="holder-name">Marco Vellani</div>
    <div class="holder-title">CEO &amp; Founder</div>
  </div>
  <div class="holder-rule"></div>

  <ul class="contact-list">
    <li class="contact-item">
      <svg viewBox="0 0 16 16" aria-hidden="true"><circle cx="8" cy="8" r="7" fill="none" stroke="var(--brand-red)" stroke-width="1.3"/><path d="M5.5 4.5 L7 6 L6.2 7.2 Q7.2 9 8.8 9.8 L10 9 L11.5 10.5 L10.5 11.6 Q6.5 11 4.4 5.5 Z" fill="var(--brand-red)"/></svg>
      <span>+34 600.218.754</span>
    </li>
    <li class="contact-item">
      <svg viewBox="0 0 16 16" aria-hidden="true"><rect x="1" y="3.5" width="14" height="9" fill="none" stroke="var(--brand-red)" stroke-width="1.3"/><path d="M1 3.5 L8 9 L15 3.5" fill="none" stroke="var(--brand-red)" stroke-width="1.3"/></svg>
      <span>vellani@alpinecounsel.com</span>
    </li>
    <li class="contact-item">
      <svg viewBox="0 0 16 16" aria-hidden="true"><circle cx="8" cy="8" r="7" fill="var(--brand-red)"/><path d="M1 8 H15 M8 1 V15 M8 1 Q3.5 8 8 15 M8 1 Q12.5 8 8 15 M2.5 4.5 H13.5 M2.5 11.5 H13.5" fill="none" stroke="#fff" stroke-width="0.9"/></svg>
      <span>www.<span class="web-domain">alpinecounsel</span>.com</span>
    </li>
  </ul>
</section>

</body>
</html>
```